K9 Orbit needs a business card designed

We need a business card designed for K9 Orbit, an expansion of K9 Systems Pty Ltd (www.k9systems.com.au)

We provide high quality professional services for the Australian space industry. Our clients include the Southern Launch Bureau and companies working in the space industry. We identify people with space related skills both locally and internationally who are then contracted by clients to create products and support space launch activities.

Colours to be used:
- Navy blue #000080
- Rocket metallic #8A7F8D
- Platinum #E5E4E2
- Black #000000
- White #FFFFFF

*Front of the card*
I have attached our K9 Orbit logo, which needs to be the main item on the card. The 'Space' text should be placed to the right of the 'K9' part rather than below, similar to the attached K9 Systems card, which this card should match.

If subtext is included, however, it should read ‘Labour Hire • Consultancy • Project Delivery’ rather than the ‘Design • Build • Test • Maintain’ of the K9 Systems card.

A black background (rather than blue background in the K9 Systems card) might be good, with a white pattern as in the K9 Systems card. If colour is used, the logo should be in its standard colours (as provided for the K9 Orbit logo).

*Back of the card*
Include a smaller K9 Orbit logo on the back.

We need the following details for K9 Orbit personnel (as a template for entry):
- Name
- Company Position
- Mobile Number
- Email
- Office Address
- Include the K9 Orbit website: www.k9orbit.com.au

Overall, we'd like to see a design that communicates the adventure of space, professional integrity, and customer service. We look forward to seeing what you can come up with.

Target Market(s)

We provide high quality professional services for the Australian space industry. Our clients include the Southern Launch Bureau and companies working in the space industry.

Contact Information for Business Card

- Name
- Company Position
- Mobile Number
- Email
- Office Address

Requirements
Must have
• See project description.

```html
<!DOCTYPE html>
<html lang="en">
<head>
<meta charset="utf-8">
<title>K9 Orbit Business Card</title>
<link href="https://fonts.googleapis.com/css2?family=Montserrat:wght@400;500;600;700&family=Lato:wght@400;700&display=swap" rel="stylesheet">
<style>
  :root {
    --navy: #1f1c66;
    --navy-deep: #17145a;
    --navy-soft: #2a2780;
    --metallic: #8a7f8d;
    --platinum: #e5e4e2;
    --white: #ffffff;
    --backdrop: #2a2a2c;
  }
  * { box-sizing: border-box; margin: 0; padding: 0; }
  html, body { width: 1200px; height: 900px; overflow: hidden; }
  body {
    background: var(--backdrop);
    font-family: "Montserrat", sans-serif;
    position: relative;
  }
  .card {
    position: absolute;
    left: 280px;
    width: 640px;
    height: 366px;
    border-radius: 22px;
    overflow: hidden;
    box-shadow: 0 14px 30px rgba(0,0,0,0.45);
  }
  .card-front {
    top: 48px;
    background: radial-gradient(ellipse at 45% 55%, var(--navy-soft) 0%, var(--navy) 55%, var(--navy-deep) 100%);
    color: var(--white);
  }
  .front-lockup {
    position: absolute;
    left: 0; right: 0; top: 128px;
    display: flex;
    align-items: center;
    justify-content: center;
    gap: 26px;
  }
  .brand-mark {
    font-family: "Montserrat", sans-serif;
    font-weight: 700;
    font-size: 40px;
    letter-spacing: 1px;
  }
  .brand-word {
    font-weight: 500;
    font-size: 54px;
    letter-spacing: 26px;
  }
  .front-tagline {
    position: absolute;
    left: 0; right: 0; top: 232px;
    text-align: center;
    font-size: 15px;
    font-weight: 500;
    letter-spacing: 1px;
  }
  .front-tagline .sep { margin: 0 10px; }

  .card-back {
    top: 486px;
    background: var(--navy);
  }
  .back-shape { position: absolute; inset: 0; }
  .back-logo {
    position: absolute;
    left: 56px; top: 150px;
    display: flex;
    align-items: center;
    gap: 14px;
    color: var(--navy);
  }
  .back-logo .dot {
    width: 16px; height: 16px;
    border-radius: 50%;
    background: var(--metallic);
  }
  .back-logo .brand-mark { font-size: 46px; }
  .back-info {
    position: absolute;
    right: 34px; top: 26px;
    width: 300px;
    text-align: right;
    color: var(--white);
  }
  .back-word {
    font-size: 38px;
    font-weight: 500;
    letter-spacing: 18px;
    margin-right: -18px;
  }
  .back-tagline {
    font-size: 7.5px;
    letter-spacing: 0.3px;
    color: var(--platinum);
    margin-top: 2px;
  }
  .person-name {
    margin-top: 18px;
    font-size: 21px;
    font-weight: 700;
    letter-spacing: 1px;
  }
  .person-title {
    font-size: 14px;
    font-weight: 400;
  }
  .address {
    margin-top: 16px;
    font-family: "Lato", sans-serif;
    font-size: 13.5px;
    line-height: 1.35;
  }
  .contacts {
    margin-top: 14px;
    list-style: none;
    font-family: "Lato", sans-serif;
    font-size: 13.5px;
    line-height: 1.55;
  }
  .contacts li {
    display: flex;
    justify-content: flex-end;
    align-items: center;
    gap: 8px;
  }
  .contacts svg { width: 12px; height: 12px; fill: var(--white); }
</style>
</head>
<body>

<section class="card card-front" aria-label="Card front">
  <div class="front-lockup">
    <span class="brand-mark">K9</span>
    <span class="brand-word">ORBIT</span>
  </div>
  <p class="front-tagline">
    Consultancy<span class="sep">•</span>Command<span class="sep">•</span>Control<span class="sep">•</span>Communications<span class="sep">•</span>Labour Hire
  </p>
</section>

<section class="card card-back" aria-label="Card back">
  <svg class="back-shape" viewBox="0 0 640 366" preserveAspectRatio="none" aria-hidden="true">
    <path d="M0,40 C120,10 330,40 410,120 C470,180 500,270 505,366 L0,366 Z" fill="var(--metallic)"/>
    <path d="M0,40 C110,12 300,40 380,125 C435,185 462,270 468,366 L0,366 Z" fill="var(--white)"/>
  </svg>

  <div class="back-logo">
    <span class="dot"></span>
    <span class="brand-mark">K9 ORBIT</span>
  </div>

  <div class="back-info">
    <div class="back-word">ORBIT</div>
    <div class="back-tagline">Consultancy • Control • Communications • Labour Hire</div>
    <div class="person-name">LENA HARTLEY</div>
    <div class="person-title">Co-Founder</div>
    <p class="address">48 Meridian Parade<br>SE | Suite 210 Adelaide 5000</p>
    <ul class="contacts">
      <li>(08) 7000 1234
        <svg viewBox="0 0 24 24"><path d="M6.6 10.8a15 15 0 0 0 6.6 6.6l2.2-2.2c.3-.3.7-.4 1-.2 1.1.4 2.3.6 3.6.6.6 0 1 .4 1 1V20c0 .6-.4 1-1 1A17 17 0 0 1 3 4c0-.6.4-1 1-1h3.5c.6 0 1 .4 1 1 0 1.3.2 2.5.6 3.6.1.3 0 .7-.2 1z"/></svg>
      </li>
      <li>hello@k9orbitmail.com
        <svg viewBox="0 0 24 24"><path d="M2 5h20v14H2z M2 5l10 8 10-8" fill="none" stroke="#fff" stroke-width="2"/></svg>
      </li>
      <li>www.k9orbit.com.au
        <svg viewBox="0 0 24 24"><circle cx="12" cy="12" r="9" fill="none" stroke="#fff" stroke-width="2"/><path d="M3 12h18M12 3c3 3 3 15 0 18M12 3c-3 3-3 15 0 18" fill="none" stroke="#fff" stroke-width="1.5"/></svg>
      </li>
    </ul>
  </div>
</section>

</body>
</html>
```